Australia Banner

Use same measuremenbts used for portugal, but ad to say something about 120,000+ New listings now available in Australia
Updates

the 2 banners should be the following sizes 448x81px 197x650px using gif format saying to click here for over 120000 new Australian Listings

look at the website www.tallowhomestead.com and check the portugal banner on the right, the australia banner will be on the left, and within the site on the top area mentioning agent offer. Use a graphic and GIF preferred.

```html
<!DOCTYPE html>
<html lang="en">
<head>
<meta charset="utf-8">
<title>Australia Listings Banners</title>
<link rel="stylesheet" href="https://fonts.googleapis.com/css2?family=Archivo+Black&display=swap">
<style>
  :root {
    --page: #ffffff;
    --ink: #000000;
    --text: #ffffff;
    --green: #6f9a33;
    --green-light: #84b040;
    --green-dark: #557a22;
    --sea: #a9c9e6;
    --land: #d6e3b0;
    --land-warm: #e6e0b8;
    --cursor: #e0201a;
    --frame: #3a3a3a;
  }
  * { margin: 0; padding: 0; box-sizing: border-box; }
  html, body {
    width: 1200px; height: 1188px; overflow: hidden;
    background: var(--page);
  }
  .stage {
    position: relative;
    width: 820px; height: 812px;
    transform: scale(1.4634);
    transform-origin: 0 0;
    font-family: "Archivo Black", "Arial Black", sans-serif;
    color: var(--text);
    text-transform: uppercase;
  }
  .shadowed { text-shadow: 1px 2px 2px rgba(0,0,0,.85); }

  /* Skyscraper 197 x 650 */
  .banner-tall {
    position: absolute; left: 72px; top: 81px;
    width: 197px; height: 650px;
    background: var(--ink);
    overflow: hidden;
  }
  .banner-tall .map-area {
    position: absolute; left: 0; top: 0; width: 197px; height: 185px;
    background:
      linear-gradient(to bottom, rgba(0,0,0,0) 0%, rgba(0,0,0,0) 78%, var(--ink) 100%),
      radial-gradient(ellipse 58% 42% at 52% 45%, var(--land-warm) 0%, var(--land) 70%, var(--sea) 100%);
  }
  .banner-tall .cursor {
    position: absolute; left: 104px; top: 94px; width: 38px; height: 62px;
  }
  .offer-box {
    position: absolute; left: 14px; top: 240px;
    width: 170px; height: 117px;
    background: var(--green);
    text-align: center;
    white-space: nowrap;
  }
  .offer-box .offer-new { display: block; font-size: 37px; line-height: 1; margin-top: 10px; letter-spacing: 1px; }
  .offer-box .offer-count { display: block; font-size: 23px; line-height: 1; margin-top: 5px; letter-spacing: 1px; }
  .offer-box .offer-label { display: block; font-size: 18px; line-height: 1; margin-top: 7px; letter-spacing: 1.5px; }
  .headline-tall {
    position: absolute; left: 0; top: 388px; width: 197px;
    text-align: center; white-space: nowrap;
    font-size: 25px; line-height: 37.5px; letter-spacing: 1px;
  }
  .cta-button {
    position: absolute; left: 18px; top: 572px;
    width: 162px; height: 40px;
    border-radius: 5px;
    background: linear-gradient(to bottom, var(--green-light), var(--green-dark));
    font-size: 15px; letter-spacing: 1.5px;
    line-height: 40px; text-align: center; white-space: nowrap;
  }

  /* Leaderboard 448 x 81 */
  .banner-wide {
    position: absolute; left: 301px; top: 81px;
    width: 448px; height: 81px;
    background: var(--ink);
    border: 1px solid var(--frame);
    overflow: hidden;
  }
  .banner-wide .map-area {
    position: absolute; left: 0; top: 0; width: 140px; height: 81px;
    background:
      linear-gradient(to right, rgba(0,0,0,0) 0%, rgba(0,0,0,0) 75%, var(--ink) 100%),
      radial-gradient(ellipse 48% 45% at 45% 52%, var(--land-warm) 0%, var(--land) 70%, var(--sea) 100%);
  }
  .banner-wide .cursor {
    position: absolute; left: 65px; top: 40px; width: 20px; height: 34px;
  }
  .wide-count {
    position: absolute; left: 141px; top: 12px;
    width: 121px; height: 32px;
    background: var(--green);
    font-size: 17px; line-height: 32px; text-align: center; letter-spacing: .5px;
    white-space: nowrap;
  }
  .wide-label {
    position: absolute; left: 268px; top: 12px; width: 174px;
    font-size: 16px; line-height: 32px; letter-spacing: 1.5px;
    white-space: nowrap;
  }
  .headline-wide {
    position: absolute; left: 141px; top: 52px; width: 301px;
    font-size: 14px; line-height: 20px; letter-spacing: .8px; white-space: nowrap;
  }
</style>
</head>
<body>
<div class="stage">

  <section class="banner-tall" aria-label="Australia listings skyscraper banner">
    <div class="map-area" role="img" aria-label="Road map of Australia with state labels"></div>
    <svg class="cursor" viewBox="0 0 38 62" aria-hidden="true">
      <path d="M2 2 L36 38 L22 38 L30 58 L22 61 L14 41 L2 52 Z" fill="var(--cursor)" stroke="#7a0d09" stroke-width="1.5" stroke-linejoin="round"/>
    </svg>
    <div class="offer-box">
      <span class="offer-new shadowed">New</span>
      <span class="offer-count shadowed">120,000+</span>
      <span class="offer-label shadowed">Listings</span>
    </div>
    <p class="headline-tall shadowed">Now<br>Available<br>In<br>Australia</p>
    <div class="cta-button shadowed">Click Here</div>
  </section>

  <section class="banner-wide" aria-label="Australia listings leaderboard banner">
    <div class="map-area" role="img" aria-label="Road map of Australia"></div>
    <svg class="cursor" viewBox="0 0 38 62" aria-hidden="true">
      <path d="M2 2 L36 38 L22 38 L30 58 L22 61 L14 41 L2 52 Z" fill="var(--cursor)" stroke="#7a0d09" stroke-width="2" stroke-linejoin="round"/>
    </svg>
    <div class="wide-count shadowed">120,000+</div>
    <div class="wide-label shadowed">New Listings</div>
    <p class="headline-wide shadowed">Now Available in Australia</p>
  </section>

</div>
</body>
</html>
```